Banner Ad & EDM image Design Project

We need a leader board banner ad and an image for an eDM for a new range of children's sunglasses for a company based in New Zealand. The brand is call Tot Lenz and provides superior quality sunglasses to help protect children from harmful UV rays. It is more than just looking cool its about protecting their eyesight for the future. Children's eyes are more vulnerable than adults as they haven't yet developed the natural protection that adults have. 80% of a persons lifetime exposure to harmful UV rays will occur before 18 years so kids need to protect their eyes while they are young to reduce the risk of damaged eyesight later in life.

Target Market(s)

Mums with Kids 3-12 years old

Industry/Entity Type

It Company

Requirements
Must have
• 1. Static Banner ad - 728x90 (specs attached)
Tot Lenz Logo - please cut from attached " swing tag" file without balloons
Copy:
80% of harmful UV exposure occurs before they are 18.
Protect them today
WIN 1 of 10 Tot Lenz Sunglasses
Blue sky and bright sun more illustrative rather than photo. See "slide 1" attached as a guide

2. edm Image - 600 W x400 H (specs attached)
Logo
Copy:

Have you got your Children’s Eyes Covered
Did you know, 80% of your child’s lifetime exposure to harmful UV rays will occur before they are 18 years as their eyes haven’t yet developed the natural protection that adults have and that.

Cover up with Tot Lenz and give your Tot Lenz 100% protection.
• Specially designed for children aged 3-12
• UV 400 providing 100% protection
• Comply to AUS/ NZ Standard 1067 2003,
• Made from quality material that will not shatter or splinter making them safe for children.

Tot Lenz are exclusively sold in pharmacies. Check out the Tot Lenz facebook page for stockists. (need to be able to add a link)

WIN Sunglasses for your Family – Click here to enter (need to be able to add a link.
Nice to have
• Image of kids on swing - attached IMG 002
Colouring as per attached - Slide 1 and Swing Tag
Should not have
• Photos, needs to be illustrative

```html
<!DOCTYPE html>
<html lang="en">
<head>
<meta charset="utf-8">
<title>Tot Lenz – eDM image and leaderboard banner</title>
<link rel="stylesheet" href="https://fonts.googleapis.com/css2?family=Arimo:wght@700&family=PT+Sans:wght@400;700&family=PT+Sans+Narrow:wght@400;700&display=swap">
<style>
  :root {
    --stage: #2a2d30;
    --sky-deep: #1f7fe2;
    --sky-mid: #3d9cf0;
    --sky-light: #8fd0f8;
    --cloud: #e6f4fd;
    --cloud-edge: #cfe9fa;
    --navy: #1a5596;
    --ink: #1d3e66;
    --white: #ffffff;
    --sun-core: #ffe45a;
    --sun-edge: #f7a21d;
    --brand-yellow: #f9c22c;
    --badge-brown: #5a4238;
    --kid-warm: #b5673d;
    --kid-cool: #6c7a8c;
  }
  * { box-sizing: border-box; margin: 0; padding: 0; }
  html, body { width: 1200px; height: 900px; overflow: hidden; background: var(--stage); }
  .canvas { position: relative; width: 1200px; height: 900px; }

  /* eDM image */
  .edm {
    position: absolute; left: 150px; top: 60px; width: 900px; height: 603px; overflow: hidden;
    background: linear-gradient(160deg, var(--sky-deep) 0%, var(--sky-mid) 55%, var(--sky-light) 100%);
  }
  .edm-sky { position: absolute; inset: 0; }
  .edm-heading {
    position: absolute; left: 42px; top: 36px; width: 200px;
    font: 700 42px/1.05 "Arimo", Arial, sans-serif; color: var(--navy);
  }
  .edm-divider {
    position: absolute; left: 256px; top: 37px; height: 105px;
    border-left: 2px dashed var(--navy); opacity: .6;
  }
  .edm-fact {
    position: absolute; left: 290px; top: 56px; width: 530px;
    font: 400 21px/36px "PT Sans Narrow", Arial, sans-serif; color: var(--navy);
  }
  .edm-cover {
    position: absolute; left: 55px; top: 230px;
    font: 700 33px/1 "Arimo", Arial, sans-serif; color: var(--white);
  }
  .edm-brand {
    position: absolute; left: 52px; top: 290px;
    font: 700 76px/1 "Arimo", Arial, sans-serif; color: var(--brand-yellow); letter-spacing: 2px;
  }
  .edm-badge { position: absolute; left: 450px; top: 157px; width: 150px; height: 150px; }
  .edm-features {
    position: absolute; left: 72px; top: 396px; list-style: none;
    font: 400 22px/42px "PT Sans", Arial, sans-serif; color: var(--white);
  }
  .edm-features li::before { content: "•"; margin-right: 14px; }
  .edm-illustration {
    position: absolute; left: 612px; top: 150px; width: 288px; height: 390px; border-radius: 40% 40% 45% 45%;
    background: radial-gradient(ellipse at 50% 40%, var(--kid-warm) 0%, var(--kid-cool) 55%, rgba(108,122,140,0) 75%);
  }
  .edm-social {
    position: absolute; left: 861px; top: 564px; width: 21px; height: 21px;
    background: var(--navy); border-radius: 2px;
  }

  /* Leaderboard banner */
  .banner {
    position: absolute; left: 54px; top: 705px; width: 1092px; height: 135px; overflow: hidden;
    background: linear-gradient(100deg, var(--cloud) 0%, var(--sky-light) 35%, var(--sky-mid) 75%, var(--sky-deep) 100%);
  }
  .banner-sun { position: absolute; left: 150px; top: -20px; width: 200px; height: 175px; }
  .banner-brand {
    position: absolute; left: 14px; top: 38px;
    font: 700 58px/1 "Arimo", Arial, sans-serif; color: var(--brand-yellow); letter-spacing: 1px;
  }
  .banner-fact {
    position: absolute; left: 352px; top: 22px;
    font: 400 22px/1 "PT Sans Narrow", Arial, sans-serif; color: var(--ink);
  }
  .banner-cta {
    position: absolute; left: 349px; top: 55px;
    font: 700 46px/1 "Arimo", Arial, sans-serif; color: var(--ink);
  }
  .banner-illustration {
    position: absolute; left: 900px; top: 8px; width: 190px; height: 120px; border-radius: 30px;
    background: linear-gradient(90deg, rgba(255,255,255,.05), rgba(30,90,170,.35));
  }
  .banner-prize {
    position: absolute; left: 950px; top: 38px; width: 125px; text-align: center;
    font: 700 18px/24px "PT Sans Narrow", Arial, sans-serif; color: var(--white);
  }
</style>
</head>
<body>
<div class="canvas">

  <section class="edm" aria-label="Tot Lenz eDM image">
    <svg class="edm-sky" width="900" height="603" viewBox="0 0 900 603" aria-hidden="true">
      <defs>
        <radialGradient id="sun-glow" cx="50%" cy="50%" r="50%">
          <stop offset="0%" stop-color="var(--sun-core)"/>
          <stop offset="70%" stop-color="#ffd23a"/>
          <stop offset="100%" stop-color="var(--sun-edge)"/>
        </radialGradient>
      </defs>
      <g fill="#ffffff" opacity=".07">
        <polygon points="820,120 0,603 240,603"/>
        <polygon points="820,120 420,603 620,603"/>
        <polygon points="820,120 0,300 0,430"/>
      </g>
      <circle cx="818" cy="122" r="135" fill="url(#sun-glow)"/>
      <path d="M0 0 H900 V60 C860 80 820 110 770 100 C730 150 660 160 600 140 C560 200 470 210 420 180 C380 230 290 230 250 200 C200 230 110 220 70 190 C40 210 15 210 0 205 Z" fill="var(--cloud)" opacity=".92"/>
      <path d="M620 0 H900 V40 C880 70 840 75 810 60 C780 90 720 80 700 55 C670 60 640 40 620 0 Z" fill="var(--cloud-edge)" opacity=".6"/>
    </svg>

    <h2 class="edm-heading">Did You Know?</h2>
    <div class="edm-divider"></div>
    <p class="edm-fact">80% of your child’s lifetime exposure to harmful UV rays will occur before they are 18 years as their eyes haven’t yet developed the natural protection that adults have and that.</p>

    <p class="edm-cover">Cover up with</p>
    <p class="edm-brand">TOT LENZ</p>

    <svg class="edm-badge" viewBox="0 0 150 150" aria-hidden="true">
      <rect x="30" y="30" width="90" height="90" rx="10" transform="rotate(45 75 75)" fill="var(--white)" stroke="var(--badge-brown)" stroke-width="7"/>
    </svg>

    <ul class="edm-features">
      <li>Specially designed for children aged 3-12</li>
      <li>Comply to AUS/ NZ Standard 1067 2003</li>
      <li>UV 400 providing 100% protection</li>
      <li>Made from quality material</li>
    </ul>

    <div class="edm-illustration" role="img" aria-label="Illustration of a child in sunglasses on a swing"></div>
    <div class="edm-social"></div>
  </section>

  <section class="banner" aria-label="Tot Lenz leaderboard banner">
    <svg class="banner-sun" viewBox="0 0 200 175" aria-hidden="true">
      <circle cx="100" cy="88" r="80" fill="var(--sun-edge)"/>
      <circle cx="72" cy="78" r="78" fill="var(--cloud)"/>
    </svg>
    <p class="banner-brand">TOT LENZ</p>
    <p class="banner-fact">80% of harmful UV exposure occurs before they are 18</p>
    <p class="banner-cta">Protect them Today</p>
    <div class="banner-illustration" role="img" aria-label="Faint illustration of children's sunglasses"></div>
    <p class="banner-prize">WIN 1 of 10<br>TOT LENZ<br>Sunglasses</p>
  </section>

</div>
</body>
</html>
```